Designing a Chocolate Bar's Package

We are a chocolate manufacturing company located in Lebanon. We produce chocolate on a wholesale level, and we are planning a new line of production at the moment.
We intend to be make small chocolate bars (about 30g) similar to the "Brasko Supreme" bar with several flavors. 2 flavors have been decided so far (Mint flavored dark chocolate and Plain dark chocolate).
The packaging material will be similar to brasko's package as well. It won't be a carton box. It'll be some sort of paper wrapping the entire bar. So I am looking for a design that has a unique and cool front and back look.
If only one design is to be prepared, please choose either the mint's flavor or the plain dark chocolate, and prepare the design accordingly.
Project Deadline Extended
Reason: I still have some time to begin the production. The new deadline,therefore, is the end of this month.
basically all chocolate lovers...
It Company
- I will be uploading our logo. Please make sure to use it in the design.

```html
<!DOCTYPE html>
<html lang="en">
<head>
<meta charset="utf-8">
<title>Corvello Chocolate + Mint Wrapper</title>
<link href="https://fonts.googleapis.com/css2?family=Archivo+Black&family=Bowlby+One&family=Arimo:wght@400;700&family=Pacifico&display=swap" rel="stylesheet">
<style>
  :root{
    --ink:#000;
    --paper:#fff;
    --teal:#1b4a55;
    --orange:#d65a36;
    --lime:#b9c43a;
    --cocoa:#2e2624;
    --cocoa-text:#2a2224;
    --tan:#b98a4a;
    --script:#1f5466;
    --rule:#c9c9c9;
    --photo-a:#e9efe0;
    --photo-b:#7a5a43;
  }
  *{margin:0;padding:0;box-sizing:border-box}
  html,body{width:1200px;height:900px;overflow:hidden;background:var(--paper)}
  .canvas{position:relative;width:1200px;height:900px}
  .band{position:absolute;left:14px;width:852px;background:var(--ink)}
  .band--top{top:20px;height:28px}
  .band--bottom{top:838px;height:32px}

  .back-panel{position:absolute;left:14px;top:48px;width:386px;height:564px;background:var(--cocoa)}
  .stripe{position:absolute;top:0;height:100%}
  .stripe--teal{left:0;width:83px;background:var(--teal)}
  .stripe--orange{left:83px;width:10px;background:var(--orange)}
  .stripe--lime{left:93px;width:11px;background:var(--lime)}

  .nutrition{position:absolute;left:125px;top:12px;width:241px;height:523px;background:var(--paper);
    padding:4px 7px;font-family:"Arimo",Arial,sans-serif;color:var(--ink);font-size:13px;line-height:1.05}
  .nutrition h2{font-family:"Arimo",Arial,sans-serif;font-weight:700;font-size:29.5px;letter-spacing:-.3px;line-height:1.05}
  .bar-thick{height:10px;background:var(--ink);margin:4px 0 3px}
  .bar-mid{height:5px;background:var(--ink);margin:4px 0 2px}
  .small-bold{font-size:9px;font-weight:700;padding:2px 0 3px;border-bottom:1px solid var(--ink)}
  .row{display:flex;justify-content:space-between;height:20.6px;align-items:center;border-bottom:1px solid #555}
  .row--indent{padding-left:15px}
  .row b{font-weight:700}
  .row:last-child{border-bottom:none}
  .dv{font-size:9px;font-weight:700;text-align:right;height:16px;line-height:16px;border-bottom:1px solid #555}
  .vitamins .row{height:21px}
  .vitamins span.dot{width:95px}
  .footnote{font-size:9px;line-height:1.12;padding-top:4px}
  .dv-table{width:100%;border-collapse:collapse;font-size:9px;line-height:1.1;margin-top:1px}
  .dv-table th{font-weight:400;text-align:left;border-bottom:1px solid var(--ink)}
  .dv-table td{padding:0}
  .dv-table tr:first-child td{padding-top:3px}
  .dv-table .ind{padding-left:7px}
  .per-gram{font-size:9px;line-height:1.15;border-top:1px solid var(--ink);margin-top:3px;padding-top:3px}
  .per-gram span{display:block;padding-left:25px}

  .story{position:absolute;left:14px;top:618px;width:386px;color:var(--cocoa-text);
    font-family:"Archivo Black",sans-serif;font-size:15.6px;line-height:22.7px}
  .story span{display:block;text-align:justify;text-align-last:justify}
  .story .script{font-family:"Pacifico",cursive;color:var(--script);font-size:16px;line-height:26px}

  .front-panel{position:absolute;left:400px;top:48px;width:422px;height:790px;border-left:1px solid var(--rule);border-right:1px solid var(--rule)}
  .flavour{position:absolute;left:40px;top:10px;font-family:"Archivo Black",sans-serif;font-size:27px;letter-spacing:6.2px;color:var(--cocoa-text);white-space:nowrap}
  .flavour .plus{color:var(--orange);letter-spacing:0}
  .flavour .mint{color:var(--lime)}
  .tagline{position:absolute;left:40px;top:42px;font-family:"Bowlby One",sans-serif;font-size:21px;line-height:28.5px;color:var(--tan);letter-spacing:.2px}
  .tagline .dark{color:var(--cocoa-text)}
  .tagline .script{font-family:"Pacifico",cursive;color:var(--script);font-size:20px}
  .tagline .dot{color:var(--orange)}
  .product-photo{position:absolute;left:56px;top:510px;width:310px;height:160px;border-radius:40px;
    background:radial-gradient(ellipse at 60% 45%,var(--photo-b) 0%,#a88366 38%,var(--photo-a) 70%,var(--paper) 100%)}
  .brand{position:absolute;left:30px;top:680px;width:400px;display:flex;align-items:center;gap:14px}
  .brand-name{font-family:"Archivo Black",sans-serif;font-size:66px;color:#4a2c1c;letter-spacing:1px;line-height:1}
  .brand-mark{width:34px;height:34px;border-radius:50%;background:var(--tan)}
</style>
</head>
<body>
<main class="canvas">
  <div class="band band--top"></div>

  <section class="back-panel">
    <div class="stripe stripe--teal"></div>
    <div class="stripe stripe--orange"></div>
    <div class="stripe stripe--lime"></div>

    <div class="nutrition">
      <h2>Nutrition Facts</h2>
      <div>Serving Size 1/2 cup (about 82g)</div>
      <div>Servings Per Container 8</div>
      <div class="bar-thick"></div>
      <div class="small-bold">Amount Per Serving</div>
      <div class="row"><span><b>Calories</b> 200</span><span>Calories from Fat 130</span></div>
      <div class="bar-mid" style="margin-top:0"></div>
      <div class="dv">% Daily Value*</div>
      <div class="row"><span><b>Total Fat</b> 14g</span><b>22%</b></div>
      <div class="row row--indent"><span>Saturated Fat 9g</span><b>45%</b></div>
      <div class="row row--indent"><span>Trans Fat 0g</span></div>
      <div class="row"><span><b>Cholesterol</b> 55mg</span><b>18%</b></div>
      <div class="row"><span><b>Sodium</b> 40mg</span><b>2%</b></div>
      <div class="row"><span><b>Total Carbohydrate</b> 17g</span><b>6%</b></div>
      <div class="row row--indent"><span>Dietary Fiber 1g</span><b>4%</b></div>
      <div class="row row--indent"><span>Sugars 14g</span></div>
      <div class="row"><span><b>Protein</b> 3g</span></div>
      <div class="bar-thick" style="margin:0 0 1px"></div>
      <div class="vitamins">
        <div class="row"><span>Vitamin A 10%</span><span class="dot">•&nbsp; Vitamin C 0%</span></div>
        <div class="row"><span>Calcium 10%</span><span class="dot">•&nbsp; Iron 6%</span></div>
      </div>
      <p class="footnote">*Percent Daily Values are based on a 2,000 calorie diet. Your daily values may be higher or lower depending on your calorie needs:</p>
      <table class="dv-table">
        <tr><th></th><th></th><th>Calories:</th><th>2,000</th><th>2,500</th></tr>
        <tr><td colspan="2">Total Fat</td><td>Less than</td><td>65g</td><td>80g</td></tr>
        <tr><td colspan="2" class="ind">Saturated Fat</td><td>Less than</td><td>20g</td><td>25g</td></tr>
        <tr><td colspan="2">Cholesterol</td><td>Less than</td><td>300mg</td><td>300 mg</td></tr>
        <tr><td colspan="2">Sodium</td><td>Less than</td><td>2,400mg</td><td>2,400mg</td></tr>
        <tr><td colspan="3">Total Carbohydrate</td><td>300g</td><td>375g</td></tr>
        <tr><td colspan="3" class="ind">Dietary Fiber</td><td>25g</td><td>30g</td></tr>
      </table>
      <p class="per-gram">Calories per gram:<span>Fat 9 &nbsp;•&nbsp; Carbohydrate 4 &nbsp;•&nbsp; Protein 4</span></p>
    </div>
  </section>

  <p class="story">
    <span class="script">At Corvello quality chocolate store,</span>
    <span>LOREM IPSUM DOLOR SIT AMET,</span>
    <span>CONSECTETUR ADIPISCING ELIT. AENEAN</span>
    <span>SODALES PORTA MAGNA NEC ADIPISCING.</span>
    <span>DONEC NEC FEUGIAT MI. INTEGER ELIT</span>
    <span>SAPIEN, ORNARE NEC PORTA SUSCIPIT,</span>
    <span>PELLENTESQUE A MASSA. SUSPENDISSE ID</span>
    <span>LIGULA ARCU. MAECENAS TINCIDUNT</span>
    <span>SOLLICITUDIN ARCU SIT AMET PULVINAR.</span>
  </p>

  <section class="front-panel">
    <h1 class="flavour">CHOCOLATE<span class="plus">+</span><span class="mint">MINT</span></h1>
    <p class="tagline">ALL THE RICHNESS OF PURE<br><span class="dark">COCOA</span> MEETS THE CRISP, COOL<br>FLAVOUR OF <span class="script">mint</span><span class="dot">.</span></p>
    <div class="product-photo" role="img" aria-label="Photo of three chocolate-coated mint cups, one cut open to show the green mint filling"></div>
    <div class="brand">
      <span class="brand-name">Corvello</span>
      <span class="brand-mark"></span>
    </div>
  </section>

  <div class="band band--bottom"></div>
</main>
</body>
</html>
```